NEW Modern Sleek Business Card for VR Language Startup

Our startup is using VR to lead the next wave of world language education. We need a two-sided business card that introduces the larger organization (Quorvel Language Inc) and our contact info on one side and shows the product, Lumidrasca, on the other side.

Side 1 (contact info)= Quorvel Logo and Contact info (name, title, phone, email)

Side 2 (product)= Lumidrasc logo, text, and website
Text= Culturally Immersive Language Learning Games
Website= www.lumidrasc.example

Target Market(s)

Education, Technology

Contact Information for Business Card

Contact info will be updated upon approval of the design. For now, put this as a placeholder.

Perry Hollins
Founder & CEO
phollins@mailtrove.example
(555)-014-2736

Font styles to use
Other font styles liked:
• Gibson and Century Gothic are the brand fonts

Requirements
Nice to have
• I would love to see cohesion between the design and colors of the two logos. I have attached a few business card designs that I like, so you can get a feel for my preferred style.

```html
<!DOCTYPE html>
<html lang="en">
<head>
<meta charset="utf-8">
<title>Lumidrasc &amp; Quorvel Language – Business Card</title>
<link rel="stylesheet" href="https://fonts.googleapis.com/css2?family=Montserrat:wght@600;700&family=Questrial&display=swap">
<style>
  :root {
    --stage: #1c1c20;
    --card-dark: #0d0d0f;
    --card-light: #ffffff;
    --ink-light: #f2f2f4;
    --ink-dark: #1b1b1d;
    --ink-muted: #55555b;
    --product-blue: #3a9be8;
    --product-violet: #6b5ce0;
    --brand-orange: #f59a3c;
    --brand-pink: #e8367a;
    --brand-violet: #7a4fd6;
    --wash-peach: #fde3d6;
    --wash-lilac: #e6e2f6;
  }
  * { box-sizing: border-box; margin: 0; padding: 0; }
  html, body { width: 1200px; height: 800px; overflow: hidden; }
  body {
    background: var(--stage);
    font-family: "Questrial", "Century Gothic", sans-serif;
    display: flex;
    align-items: center;
    justify-content: center;
    gap: 44px;
  }
  .card {
    position: relative;
    width: 540px;
    height: 310px;
    border-radius: 22px;
    overflow: hidden;
  }

  /* Product side */
  .card--product {
    background: var(--card-dark);
    color: var(--ink-light);
    padding: 36px 40px;
  }
  .product-mark {
    position: absolute;
    top: 38px;
    right: 40px;
    display: flex;
    align-items: center;
    gap: 12px;
  }
  .product-mark__dot {
    width: 22px; height: 22px; border-radius: 50%;
    background: var(--product-blue);
  }
  .product-mark__name {
    font-family: "Montserrat", sans-serif;
    font-weight: 700;
    font-size: 40px;
    color: var(--product-blue);
    letter-spacing: 0.5px;
  }
  .product-tagline {
    position: absolute;
    left: 40px;
    top: 118px;
    font-size: 25px;
    line-height: 1.3;
  }
  .product-url {
    position: absolute;
    left: 40px;
    bottom: 36px;
    font-size: 22px;
    letter-spacing: 0.5px;
  }
  .product-url__name { color: var(--product-blue); }

  /* Contact side */
  .card--contact {
    background: var(--card-light);
    color: var(--ink-dark);
  }
  .contact-wash {
    position: absolute;
    right: -60px;
    bottom: -80px;
    width: 420px;
    height: 300px;
    border-radius: 50% 50% 0 0;
    background: linear-gradient(160deg, var(--wash-peach), var(--wash-lilac));
    opacity: 0.8;
  }
  .brand-mark {
    position: absolute;
    top: 40px;
    left: 40px;
    display: flex;
    align-items: center;
    gap: 14px;
  }
  .brand-mark__dot {
    width: 24px; height: 24px; border-radius: 50%;
    background: var(--brand-pink);
  }
  .brand-mark__name {
    font-family: "Montserrat", sans-serif;
    font-weight: 700;
    font-size: 40px;
    letter-spacing: 6px;
    color: var(--ink-dark);
  }
  .brand-sub {
    position: absolute;
    top: 94px;
    left: 78px;
    font-size: 16px;
    letter-spacing: 9px;
    color: var(--ink-muted);
  }
  .contact {
    position: absolute;
    left: 40px;
    bottom: 38px;
  }
  .contact__name {
    font-family: "Montserrat", sans-serif;
    font-weight: 700;
    font-size: 20px;
    letter-spacing: 1px;
  }
  .contact__title {
    font-size: 16px;
    color: var(--ink-muted);
    margin-bottom: 14px;
  }
  .contact__line {
    display: flex;
    align-items: center;
    gap: 10px;
    font-size: 15px;
    color: var(--ink-muted);
    margin-top: 6px;
  }
  .contact__icon {
    width: 20px; height: 20px; border-radius: 50%;
    background: linear-gradient(135deg, var(--brand-pink), var(--brand-violet));
    display: flex; align-items: center; justify-content: center;
  }
</style>
</head>
<body>

  <section class="card card--product" aria-label="Product side">
    <div class="product-mark">
      <span class="product-mark__dot"></span>
      <span class="product-mark__name">Lumidrasc</span>
    </div>
    <p class="product-tagline">Culturally Immersive<br>Language<br>Learning Games</p>
    <p class="product-url">www.<span class="product-url__name">lumidrasc</span>.example</p>
  </section>

  <section class="card card--contact" aria-label="Contact side">
    <div class="contact-wash"></div>
    <div class="brand-mark">
      <span class="brand-mark__dot"></span>
      <span class="brand-mark__name">QUORVEL</span>
    </div>
    <p class="brand-sub">LANGUAGE</p>
    <div class="contact">
      <p class="contact__name">PERRY HOLLINS</p>
      <p class="contact__title">Founder &amp; CEO</p>
      <p class="contact__line">
        <span class="contact__icon">
          <svg width="11" height="11" viewBox="0 0 24 24" aria-hidden="true"><path fill="#fff" d="M6.6 10.8a15 15 0 0 0 6.6 6.6l2.2-2.2a1 1 0 0 1 1-.25 11 11 0 0 0 3.6.6 1 1 0 0 1 1 1V20a1 1 0 0 1-1 1A17 17 0 0 1 3 4a1 1 0 0 1 1-1h3.5a1 1 0 0 1 1 1 11 11 0 0 0 .6 3.6 1 1 0 0 1-.25 1z"/></svg>
        </span>
        (555)-014-2736
      </p>
      <p class="contact__line">
        <span class="contact__icon">
          <svg width="11" height="11" viewBox="0 0 24 24" aria-hidden="true"><path fill="none" stroke="#fff" stroke-width="2.4" d="M3 6h18v12H3zM3 6l9 7 9-7"/></svg>
        </span>
        phollins@mailtrove.example
      </p>
    </div>
  </section>

</body>
</html>
```